Business Postcard Mailer - 2 sided - 6 x 10.5 inches

We will be purchasing multiple designs through this project. We need a postcard mailer for a residential painting business. The final design needs to have the special 15% Off, contact information, company logo, stamp indicia, and list of services. I will provide past examples and any additional logos. Company colors are #34482E and #4A1717. Old samples are provided. Final flat size should be 6 x 10.5 inches. And we will need a return address in the upper left-hand corner of the backside. QMRB Layout Guidelines are attached. 4389 Juniper Ave #7, Waukesha, WI 53947.
Updates

I just guaranteed the project and will be expecting more entries. We will also be purchasing additional designs (4-5) so we want to ensure a good variety.

Target Market(s)

Homeowners

Industry/Entity Type

Painting

Font styles to use
Sans Serif

Requirements
Must have
• Logo and brand colors
Nice to have
• Call to action - Book your free estimate at www.BrightCoatCrew.example or Call now 262-555-0147.

```html
<!DOCTYPE html>
<html lang="en">
<head>
<meta charset="utf-8">
<title>Bright Coat Crew – Spring Special Postcard</title>
<link rel="stylesheet" href="https://fonts.googleapis.com/css2?family=Open+Sans:wght@300;400;600;700;800&display=swap">
<style>
  :root{
    --green:#34482E;
    --maroon:#4A1717;
    --ink:#2b2b2b;
    --paper:#ffffff;
    --page:#f2f2f2;
    --rule:#3a3a3a;
    --badge:#b9b9b9;
  }
  *{box-sizing:border-box;margin:0;padding:0}
  html,body{width:1200px;height:1200px;overflow:hidden;background:var(--page);font-family:"Open Sans",sans-serif;color:var(--ink)}
  .card{position:absolute;left:151px;width:895px;height:530px;background:var(--paper)}
  .card--front{top:46px}
  .card--back{top:607px}

  .brand{position:absolute;display:flex;align-items:flex-start;gap:10px}
  .brand__mark{width:16px;height:16px;margin-top:8px;background:var(--maroon);flex:none}
  .brand__name{font-weight:800;font-size:28px;line-height:1.08;color:var(--green);letter-spacing:-.5px}

  .offer{position:absolute;text-align:left}
  .offer__kicker{font-weight:600;font-size:18px;letter-spacing:7px;color:var(--maroon)}
  .offer__value{font-size:66px;line-height:1;color:var(--green);margin-top:6px;font-weight:400;letter-spacing:-1px}
  .offer__value strong{font-weight:800}
  .offer__note{font-size:15px;letter-spacing:1.2px;color:var(--maroon);margin-top:10px}

  .photo{position:absolute;left:440px;top:30px;width:441px;height:346px;
    background:linear-gradient(90deg,rgba(255,255,255,1) 0%,#eeeeee 22%,#e4e3e1 60%,#dcdad7 100%)}

  .cta{position:absolute;left:14px;width:866px;height:132px;background:var(--maroon);color:#fff;padding:30px 0 0 78px}
  .card--front .cta{top:384px}
  .card--back .cta{top:385px}
  .cta__lead{font-weight:300;font-size:21px;line-height:1.3}
  .cta__action{font-weight:700;font-size:24px;line-height:1.3;letter-spacing:-.2px}

  .return-address{position:absolute;left:90px;top:143px;font-size:10px;line-height:1.3;color:var(--maroon)}

  .local{position:absolute;left:81px;top:200px;width:160px;text-align:center}
  .local svg{display:block;margin:0 auto}
  .local__text{font-weight:700;font-size:18px;line-height:1.2;color:var(--maroon);margin-top:22px}

  .services{position:absolute;left:302px;top:215px;list-style:none}
  .services li{display:flex;align-items:center;gap:10px;height:29px;font-weight:700;font-size:20px;color:var(--maroon)}

  .indicia{position:absolute;left:743px;top:67px;width:82px;height:81px;border:2px solid #111;text-align:center;font-size:9px;line-height:1.25;color:#111;padding-top:4px;font-family:Arial,sans-serif}
  .indicia__paid{font-weight:700;font-size:12.5px;border-top:1px solid #999;border-bottom:1px solid #999;margin:2px 6px;line-height:1.35}

  .address-lines{position:absolute;left:614px;top:203px;width:227px}
  .address-lines span{display:block;height:32px;border-top:1.5px solid var(--rule)}

  .badges{position:absolute;left:614px;top:323px;display:flex;gap:18px;align-items:center}
  .badges span{display:block;background:var(--badge)}
</style>
</head>
<body>

<section class="card card--front" aria-label="Postcard front">
  <div class="brand" style="left:158px;top:90px">
    <span class="brand__mark"></span>
    <span class="brand__name">Bright Coat<br>Crew</span>
  </div>

  <div class="offer" style="left:123px;top:194px">
    <p class="offer__kicker">SPRING SPECIAL</p>
    <p class="offer__value"><strong>15%</strong> OFF</p>
    <p class="offer__note">Starting March, Interior &amp; Exterior</p>
  </div>

  <div class="photo" role="img" aria-label="Photo of a smiling painter in overalls holding a brush, ladder behind him"></div>

  <div class="cta">
    <p class="cta__lead">Book your free estimate at</p>
    <p class="cta__action">www.BrightCoatCrew.example or Call now 262-555-0147.</p>
  </div>
</section>

<section class="card card--back" aria-label="Postcard back">
  <div class="brand" style="left:77px;top:66px">
    <span class="brand__mark"></span>
    <span class="brand__name">Bright Coat<br>Crew</span>
  </div>
  <p class="return-address">4389 Juniper Ave #7,Waukesha,<br>WI 53947.</p>

  <div class="offer" style="left:307px;top:66px">
    <p class="offer__kicker">SPRING SPECIAL</p>
    <p class="offer__value"><strong>15%</strong> OFF</p>
    <p class="offer__note">Starting March, Interior &amp; Exterior</p>
  </div>

  <div class="local">
    <svg width="66" height="82" viewBox="0 0 66 82" aria-hidden="true">
      <path d="M33 79 C20 62 4 48 4 31 A29 29 0 0 1 62 31 C62 48 46 62 33 79 Z" fill="none" stroke="var(--green)" stroke-width="4"/>
      <circle cx="33" cy="31" r="13" fill="none" stroke="var(--maroon)" stroke-width="6"/>
    </svg>
    <p class="local__text">LOCALLY OWNED<br>AND OPERATED</p>
  </div>

  <ul class="services">
    <li><svg width="20" height="20" viewBox="0 0 20 20" aria-hidden="true"><circle cx="10" cy="10" r="10" fill="var(--green)"/><path d="M5.5 10.5l3 3 6-6.5" fill="none" stroke="#fff" stroke-width="2.4"/></svg>Interior Painting</li>
    <li><svg width="20" height="20" viewBox="0 0 20 20" aria-hidden="true"><circle cx="10" cy="10" r="10" fill="var(--green)"/><path d="M5.5 10.5l3 3 6-6.5" fill="none" stroke="#fff" stroke-width="2.4"/></svg>Exterior Painting</li>
    <li><svg width="20" height="20" viewBox="0 0 20 20" aria-hidden="true"><circle cx="10" cy="10" r="10" fill="var(--green)"/><path d="M5.5 10.5l3 3 6-6.5" fill="none" stroke="#fff" stroke-width="2.4"/></svg>Carpentry Services</li>
    <li><svg width="20" height="20" viewBox="0 0 20 20" aria-hidden="true"><circle cx="10" cy="10" r="10" fill="var(--green)"/><path d="M5.5 10.5l3 3 6-6.5" fill="none" stroke="#fff" stroke-width="2.4"/></svg>Drywall Repair</li>
    <li><svg width="20" height="20" viewBox="0 0 20 20" aria-hidden="true"><circle cx="10" cy="10" r="10" fill="var(--green)"/><path d="M5.5 10.5l3 3 6-6.5" fill="none" stroke="#fff" stroke-width="2.4"/></svg>Financing Available</li>
  </ul>

  <div class="indicia">
    <p>Presorted<br>Standard<br>U.S. Postage</p>
    <p class="indicia__paid">PAID</p>
    <p>NMX</p>
  </div>

  <div class="address-lines" aria-hidden="true"><span></span><span></span><span></span><span></span></div>

  <div class="badges" aria-label="Membership badges">
    <span style="width:34px;height:38px"></span>
    <span style="width:36px;height:36px"></span>
    <span style="width:36px;height:28px"></span>
    <span style="width:38px;height:16px"></span>
    <span style="width:40px;height:16px"></span>
  </div>

  <div class="cta">
    <p class="cta__lead">Book your free estimate at</p>
    <p class="cta__action">www.BrightCoatCrew.example or Call now 262-555-0147.</p>
  </div>
</section>

</body>
</html>
```